Brasko Construction Business Card

I need a business card design for my company.
We are a construction/machinery company.
I would like to see my logo on the front of the card and my details on the other side
I would like the card to be black or dark grey in colour,with my logo as i send it or modified with a lighter blue colour
I would like to see the design kept fairly simple,but eye catching at the same time
Industry/Entity Type
Business
Contact Information for Business Card
Name
Phone Number
Address
Email
Colors
00a990
1b1b1b
000000
474747
ececec

```html
<!DOCTYPE html>
<html lang="en">
<head>
<meta charset="utf-8">
<title>Brasko Construction Business Card</title>
<link rel="stylesheet" href="https://fonts.googleapis.com/css2?family=Questrial&display=swap">
<style>
  :root {
    --teal: #00a990;
    --ink: #1b1b1b;
    --black: #000000;
    --grey: #474747;
    --paper: #ffffff;
    --light: #ececec;
    --backdrop: #d6d2cb;
  }
  * { margin: 0; padding: 0; box-sizing: border-box; }
  html, body {
    width: 1200px; height: 900px; overflow: hidden;
    background: var(--backdrop);
    font-family: "Questrial", "Century Gothic", sans-serif;
  }
  .card {
    position: absolute;
    width: 620px; height: 354px;
    left: 290px;
    box-shadow: 0 10px 24px rgba(0,0,0,.25);
    overflow: hidden;
  }
  .card-front {
    top: 50px;
    background: linear-gradient(135deg, #2a2a2a 0%, var(--ink) 45%, var(--black) 100%);
    display: flex; align-items: center; justify-content: center;
  }
  .card-back { top: 480px; background: var(--paper); }

  .brand { color: var(--teal); text-transform: uppercase; font-weight: 400; text-align: center; line-height: 1; }
  .brand-mark { width: 34px; height: 34px; background: var(--teal); margin: 0 auto 14px; }
  .brand-name { font-size: 58px; letter-spacing: 3px; }
  .brand-sub { font-size: 23px; letter-spacing: 6px; margin-top: 6px; }

  .card-back .brand { position: absolute; right: 34px; top: 26px; }
  .card-back .brand-mark { width: 20px; height: 20px; margin-bottom: 8px; }
  .card-back .brand-name { font-size: 36px; letter-spacing: 2px; }
  .card-back .brand-sub { font-size: 14px; letter-spacing: 4px; margin-top: 4px; }

  .holder { position: absolute; left: 44px; top: 148px; }
  .holder-name { font-size: 30px; color: var(--ink); letter-spacing: .5px; }
  .holder-role { font-size: 16px; color: var(--teal); margin-top: 4px; }
  .divider { position: absolute; left: 150px; right: 30px; top: 203px; height: 2px; background: var(--ink); }

  .contacts { position: absolute; left: 50px; top: 222px; list-style: none; }
  .contact {
    border-left: 2px solid var(--teal);
    padding-left: 6px; margin-bottom: 8px;
    font-size: 16px; color: var(--ink); line-height: 1.1;
  }
  .contact svg { display: block; width: 12px; height: 11px; fill: var(--teal); margin-bottom: 2px; }

  .footer-band { position: absolute; left: 0; bottom: 0; width: 620px; height: 48px; }
</style>
</head>
<body>
  <section class="card card-front">
    <div class="brand">
      <div class="brand-mark"></div>
      <div class="brand-name">Brasko</div>
      <div class="brand-sub">Construction</div>
    </div>
  </section>

  <section class="card card-back">
    <div class="brand">
      <div class="brand-mark"></div>
      <div class="brand-name">Brasko</div>
      <div class="brand-sub">Construction</div>
    </div>

    <div class="holder">
      <div class="holder-name">Your Name</div>
      <div class="holder-role">Owner</div>
    </div>
    <div class="divider"></div>

    <ul class="contacts">
      <li class="contact">
        <svg viewBox="0 0 12 11"><path d="M1 3C1 1 3 0 6 0s5 1 5 3v1H8V3H4v1H1z M2 5h8l1 6H1z"/></svg>
        00 0000 0000
      </li>
      <li class="contact">
        <svg viewBox="0 0 12 11"><path d="M6 0a4 4 0 0 1 4 4c0 3-4 7-4 7S2 7 2 4a4 4 0 0 1 4-4zm0 2.5a1.5 1.5 0 1 0 0 3 1.5 1.5 0 0 0 0-3z"/></svg>
        00, Any St. Anywhere, Somewhere-0000
      </li>
      <li class="contact">
        <svg viewBox="0 0 12 11"><path d="M0 1h12v1L6 6 0 2z M0 3.5l6 4 6-4V10H0z"/></svg>
        youremail@xyz.com
      </li>
    </ul>

    <svg class="footer-band" viewBox="0 0 620 48" preserveAspectRatio="none">
      <polygon points="0,30 420,30 432,16 620,16 620,32 0,38" fill="var(--teal)"/>
      <rect x="0" y="36" width="620" height="12" fill="var(--ink)"/>
      <polygon points="0,38 620,32 620,36 0,40" fill="var(--ink)"/>
    </svg>
  </section>
</body>
</html>
```